Harbourgate Earthmoving – Website Design Brief

Web Design Brief

We are seeking a web designer to build a modern, responsive website for Harbourgate Earthmoving, a Sydney-based earthworks and excavation company.

2. Project Goal
- Build a professional, easy-to-navigate website that:
- Showcases HGE’s capabilities and past projects
- Attracts residential and commercial developers
- Builds credibility and encourages enquiries

3. Target Audience
- Residential developers and home builders
- Commercial construction firms
- Project managers seeking reliable excavation & plant hire services

4. Services to Highlight
- Bulk Excavation
- Detailed Excavation
- Demolition
- Shoring
- Plant Hire

5. Brand Style & Tone
- Clean, bold, and modern
- Professional with a “we get the job done” attitude
- Colors: Lime Green + Concrete Grey (from logo)
- Fonts: Match the modern, rounded, bold typeface in the logo
- Imagery: Showcase big machines, on-site work, before & after shots

6. Website Pages
Recommended structure:
- Home – Quick intro, project highlights, CTA
- About Us – Team story, mission, safety focus
- Services – Separate sections for each core service
- Projects – Case studies or photo gallery
- Plant Hire – Machines available, specs/photos
- Contact – Form + map + details

7. Assets Provided
- Logo (both long + stacked formats)
- Project photos. More can be provided if required.
- Copy: To be drafted

8. Deliverables
Responsive website (desktop/mobile/tablet)
- SEO-ready structure
- CMS (WordPress) for future edits
- Google Maps integration, job enquiry form

Target Market(s)

Target Audience Residential developers and home builders Commercial construction firms Project managers seeking reliable excavation & plant hire services

Industry/Entity Type

Construction

Number of Pages Required

1 page

Requirements
Must have
• Build a professional, easy-to-navigate website that: Showcases HGE’s capabilities and past projects Attracts residential and commercial developers Builds credibility and encourages enquiries
Nice to have
• All provided in the Description
Should not have

```html
<!DOCTYPE html>
<html lang="en">
<head>
<meta charset="utf-8">
<title>Harbourgate Earthmoving</title>
<link rel="stylesheet" href="https://fonts.googleapis.com/css2?family=Michroma&family=Poppins:wght@400;500;600&display=swap">
<style>
:root{
  --lime:#8cc63f;
  --lime-dark:#6fa82e;
  --ink:#1c1c1c;
  --charcoal:#222222;
  --field:#333333;
  --white:#ffffff;
  --muted:#cfcfcf;
}
*{box-sizing:border-box;margin:0;padding:0}
html,body{width:1200px;height:4056px;overflow:hidden}
body{position:relative;background:var(--ink);font-family:"Poppins",sans-serif;color:var(--white)}
.abs{position:absolute}
.display{font-family:"Michroma",sans-serif;font-weight:400;letter-spacing:1px;text-transform:uppercase}
.btn{position:absolute;display:flex;align-items:center;justify-content:center;border-radius:999px;font-family:"Poppins",sans-serif;font-weight:500;text-transform:uppercase;font-size:17px}
.btn-solid{background:var(--lime);color:var(--white)}
.photo{position:absolute}

/* hero */
.hero-bg{position:absolute;left:0;top:0;width:1200px;height:780px}
.nav{position:absolute;left:32px;top:43px;width:1121px;height:78px;background:var(--white);border-radius:40px}
.nav-logo{position:absolute;left:42px;top:29px;width:270px;white-space:nowrap;font-family:"Poppins",sans-serif;font-weight:600;font-size:15px;line-height:20px;color:var(--lime);text-transform:uppercase;letter-spacing:.5px}
.nav-link{position:absolute;top:30px;font-size:14px;font-weight:500;color:var(--ink);text-transform:uppercase}
.nav-cta{left:926px;top:20px;width:163px;height:41px;font-size:17px}
.hero-title{left:74px;top:282px;font-size:40px;line-height:52px;color:var(--ink);white-space:nowrap}
.hero-text{left:74px;top:413px;width:440px;font-size:10.5px;line-height:14px;color:var(--ink)}
.hero-btn{left:74px;top:480px;width:164px;height:41px;border:2px solid var(--ink);color:var(--ink);font-size:16px}

/* about */
.about-ring{position:absolute;left:74px;top:830px;width:372px;height:372px;border-radius:50%;background:var(--lime)}
.about-photo{left:91px;top:843px;width:346px;height:346px;border-radius:50%;background:linear-gradient(160deg,#b8c0c8 0%,#8d8a7d 45%,#6b5e4f 75%,#d9d9d9 100%)}
.about-title{left:548px;top:905px;font-size:48px;line-height:58px}
.about-text{left:548px;top:976px;width:525px;font-size:12.5px;line-height:17px;color:var(--white)}
.about-btn{left:542px;top:1104px;width:178px;height:44px}

/* services */
.services-bg{left:0;top:1302px;width:1200px;height:667px;background:linear-gradient(120deg,#1f2632 0%,#2a2a28 40%,#4a3a18 75%,#6a4c10 100%)}
.section-title{position:absolute;left:0;width:1200px;text-align:center;font-size:50px;line-height:60px}
.service-card{top:1580px;width:263px;height:305px}
.service-label{position:absolute;top:1902px;width:263px;text-align:center;font-size:17px;font-weight:600}
.arrow{position:absolute;top:1711px;width:58px;height:58px}

/* portfolio */
.tile{position:absolute}
.view-btn{left:507px;top:2763px;width:178px;height:44px}

/* quote */
.quote-bg{left:0;top:2848px;width:1200px;height:720px;background:linear-gradient(180deg,#1d221d 0%,#262a22 50%,#2e3226 100%)}
.field{position:absolute;background:var(--field);border-radius:30px;padding-left:20px;display:flex;align-items:center;font-size:15px;color:var(--muted)}
.field-area{align-items:flex-start;padding-top:24px;padding-left:28px}
.quote-btn{left:261px;top:3350px;width:717px;height:55px;font-size:17px}

/* footer */
.footer-svg{position:absolute;left:0;top:3440px;width:1200px;height:616px}
.foot-logo{position:absolute;left:90px;top:3737px;width:134px;height:96px;background:var(--white);display:flex;align-items:center;justify-content:center;text-align:center;color:var(--lime);font-weight:600;font-size:14px;line-height:18px;text-transform:uppercase}
.social{position:absolute;top:3875px;width:26px;height:26px;border-radius:50%;background:var(--ink)}
.foot-heading{position:absolute;font-size:22px;color:var(--ink)}
.foot-links{position:absolute;left:454px;top:3770px;list-style:none}
.foot-links li{display:flex;align-items:center;height:35px;font-size:18px;color:var(--ink)}
.foot-links svg{margin-right:10px}
.contact-item{position:absolute;left:806px;display:flex;align-items:center;font-size:17px;color:var(--ink);white-space:nowrap}
.contact-item svg{margin-right:16px}
.foot-rule{position:absolute;left:99px;top:3974px;width:981px;height:1px;background:var(--ink)}
.foot-small{position:absolute;top:4009px;font-size:14px;color:var(--ink)}
</style>
</head>
<body>

<!-- Hero -->
<svg class="hero-bg" viewBox="0 0 1200 780" aria-hidden="true">
  <defs>
    <linearGradient id="heroGreen" x1="0" y1="0" x2="1" y2="1">
      <stop offset="0" stop-color="#93cb4a"/>
      <stop offset="0.5" stop-color="#86c040"/>
      <stop offset="1" stop-color="#9bd052"/>
    </linearGradient>
  </defs>
  <path d="M0 0H1200V575Q600 880 0 583Z" fill="url(#heroGreen)"/>
  <path d="M205 690Q610 800 1016 672Q620 770 205 690Z" fill="#111"/>
  <path d="M205 690Q610 790 1016 672Q610 820 205 690Z" fill="var(--lime)"/>
</svg>

<nav class="nav">
  <div class="nav-logo">Harbourgate Earthmoving</div>
  <span class="nav-link" style="left:344px">Home</span>
  <span class="nav-link" style="left:423px">About</span>
  <span class="nav-link" style="left:522px">Services</span>
  <span class="nav-link" style="left:637px">Projects</span>
  <span class="nav-link" style="left:757px">Plant Hire</span>
  <span class="btn btn-solid nav-cta">Contact Us</span>
</nav>

<h1 class="abs display hero-title">Harbourgate<br>Earthmoving</h1>
<p class="abs hero-text">Lorem ipsum dolor sit amet, consectetur adipiscing elit, sed do eiusmod tempor incididunt ut labore et dolore magna aliqua. Ut enim ad minim veniam, quis nostrud exercitation ullamco laboris nisi ut aliquip ex ea commodo consequat.</p>
<span class="btn hero-btn">Get a Quote</span>

<div class="photo" role="img" aria-label="Tracked excavator with extended boom and bucket" style="left:600px;top:262px;width:550px;height:376px;border-radius:40px 40px 20px 20px;background:linear-gradient(135deg,#4a4a4a 0%,#3a3a3a 45%,#c9a21e 70%,#2b2b2b 100%);opacity:.9"></div>

<!-- About -->
<div class="about-ring"></div>
<div class="photo about-photo" role="img" aria-label="Excavator and truck on a demolition site"></div>
<h2 class="abs display about-title">About Us</h2>
<p class="abs about-text">Lorem ipsum dolor sit amet, consectetur adipiscing elit, sed do eiusmod tempor incididunt ut labore et dolore magna aliqua. Ut enim ad minim veniam, quis nostrud exercitation ullamco laboris nisi ut aliquip ex ea commodo consequat. Duis aute irure dolor in reprehenderit in voluptate velit esse cillum dolore eu fugiat nulla pariatur. Excepteur sint occaecat cupidatat non proident, sunt in culpa qui officia deserunt mollit anim id est laborum.</p>
<span class="btn btn-solid about-btn">Read More</span>

<!-- Services -->
<div class="photo services-bg" role="img" aria-label="Dark close-up of excavator machinery"></div>
<h2 class="display section-title" style="top:1441px">Our Services</h2>

<div class="photo service-card" role="img" aria-label="Excavator bucket for bulk excavation" style="left:172px;background:linear-gradient(160deg,#c39a3a,#6b5a3a 55%,#3d3426)"></div>
<div class="photo service-card" role="img" aria-label="Excavator on a demolition site" style="left:465px;background:linear-gradient(180deg,#4e6a4a,#8a7450 50%,#a8855a)"></div>
<div class="photo service-card" role="img" aria-label="Excavator on grassy plant hire site at sunset" style="left:758px;background:linear-gradient(180deg,#e8e0c8,#d9a93e 45%,#7c9a48)"></div>
<div class="service-label" style="left:164px">Bulk Excavation</div>
<div class="service-label" style="left:462px">Demolition</div>
<div class="service-label" style="left:766px">Plant Hire</div>

<svg class="arrow" style="left:77px" viewBox="0 0 58 58" aria-hidden="true">
  <circle cx="29" cy="29" r="27" fill="none" stroke="var(--lime)" stroke-width="2"/>
  <path d="M34 17L22 29L34 41" fill="none" stroke="var(--lime)" stroke-width="2.5"/>
</svg>
<svg class="arrow" style="left:1050px" viewBox="0 0 58 58" aria-hidden="true">
  <circle cx="29" cy="29" r="27" fill="none" stroke="var(--lime)" stroke-width="2"/>
  <path d="M24 17L36 29L24 41" fill="none" stroke="var(--lime)" stroke-width="2.5"/>
</svg>

<!-- Portfolio -->
<h2 class="display section-title" style="top:2074px">Our Portfolio</h2>
<div class="tile" role="img" aria-label="White company ute" style="left:169px;top:2214px;width:274px;height:156px;background:linear-gradient(180deg,#d8dde0,#f2f2f2 55%,#3a3a3a)"></div>
<div class="tile" role="img" aria-label="Excavator and truck on demolition site" style="left:460px;top:2214px;width:276px;height:334px;background:linear-gradient(170deg,#b6bec6,#8e8466 45%,#6f5c48 75%,#d5d5d5)"></div>
<div class="tile" role="img" aria-label="Excavated trench with sandy soil" style="left:758px;top:2214px;width:275px;height:156px;background:linear-gradient(160deg,#a08560,#c4a27a 50%,#8a6e4c)"></div>
<div class="tile" role="img" aria-label="White tipper truck under trees" style="left:169px;top:2383px;width:274px;height:331px;background:linear-gradient(180deg,#3f5a3a,#6a7a5a 40%,#d9d9d9 65%,#444)"></div>
<div class="tile" role="img" aria-label="Brick house behind site fencing" style="left:460px;top:2561px;width:276px;height:153px;background:linear-gradient(180deg,#5a6e4a,#7a4a3a 45%,#8a7c6a)"></div>
<div class="tile" role="img" aria-label="Excavator tracks on dirt" style="left:758px;top:2383px;width:275px;height:331px;background:linear-gradient(160deg,#8c7a62,#5a4e42 55%,#a08a6e)"></div>
<span class="btn btn-solid view-btn">View All</span>

<!-- Quote -->
<div class="photo quote-bg" role="img" aria-label="Dim construction site with machinery at dusk"></div>
<h2 class="display section-title" style="top:2974px;left:12px">Get a Quote</h2>
<div class="field" style="left:265px;top:3095px;width:340px;height:42px">Your Name</div>
<div class="field" style="left:643px;top:3095px;width:338px;height:42px">Your Phone</div>
<div class="field" style="left:265px;top:3166px;width:340px;height:42px">Email Address</div>
<div class="field" style="left:643px;top:3166px;width:338px;height:42px">Select Service</div>
<div class="field field-area" style="left:265px;top:3233px;width:716px;height:90px">Additional Message</div>
<span class="btn btn-solid quote-btn">Get an Appointment Now</span>

<!-- Footer -->
<svg class="footer-svg" viewBox="0 3440 1200 616" aria-hidden="true">
  <path d="M0 3690Q560 3470 1200 3650V4056H0Z" fill="var(--lime)"/>
  <path d="M190 3605Q620 3450 1200 3680V3640Q620 3470 190 3605Z" fill="#111"/>
  <path d="M190 3600Q620 3440 1150 3595Q620 3465 190 3600Z" fill="var(--lime)"/>
</svg>

<div class="foot-logo">Harbourgate<br>Earth-<br>moving</div>
<span class="social" style="left:94px" aria-label="Social profile"></span>
<span class="social" style="left:157px" aria-label="Social profile"></span>
<span class="social" style="left:223px" aria-label="Social profile"></span>

<div class="foot-heading display" style="left:454px;top:3728px">Quick Links</div>
<ul class="foot-links">
  <li><svg width="14" height="14" viewBox="0 0 14 14"><circle cx="7" cy="7" r="6" fill="none" stroke="#1c1c1c" stroke-width="1.4"/><path d="M4 7H10M7.5 4.5L10 7L7.5 9.5" fill="none" stroke="#1c1c1c" stroke-width="1.4"/></svg>Home</li>
  <li><svg width="14" height="14" viewBox="0 0 14 14"><circle cx="7" cy="7" r="6" fill="none" stroke="#1c1c1c" stroke-width="1.4"/><path d="M4 7H10M7.5 4.5L10 7L7.5 9.5" fill="none" stroke="#1c1c1c" stroke-width="1.4"/></svg>About</li>
  <li><svg width="14" height="14" viewBox="0 0 14 14"><circle cx="7" cy="7" r="6" fill="none" stroke="#1c1c1c" stroke-width="1.4"/><path d="M4 7H10M7.5 4.5L10 7L7.5 9.5" fill="none" stroke="#1c1c1c" stroke-width="1.4"/></svg>Services</li>
  <li><svg width="14" height="14" viewBox="0 0 14 14"><circle cx="7" cy="7" r="6" fill="none" stroke="#1c1c1c" stroke-width="1.4"/><path d="M4 7H10M7.5 4.5L10 7L7.5 9.5" fill="none" stroke="#1c1c1c" stroke-width="1.4"/></svg>Projects</li>
  <li><svg width="14" height="14" viewBox="0 0 14 14"><circle cx="7" cy="7" r="6" fill="none" stroke="#1c1c1c" stroke-width="1.4"/><path d="M4 7H10M7.5 4.5L10 7L7.5 9.5" fill="none" stroke="#1c1c1c" stroke-width="1.4"/></svg>Contact</li>
</ul>

<div class="foot-heading display" style="left:810px;top:3724px">Contact Info</div>
<div class="contact-item" style="top:3772px">
  <svg width="28" height="28" viewBox="0 0 24 24"><path d="M6.6 10.8a15.1 15.1 0 0 0 6.6 6.6l2.2-2.2a1 1 0 0 1 1-.25 11.4 11.4 0 0 0 3.6.57 1 1 0 0 1 1 1V20a1 1 0 0 1-1 1A17 17 0 0 1 3 4a1 1 0 0 1 1-1h3.5a1 1 0 0 1 1 1c0 1.25.2 2.45.57 3.57a1 1 0 0 1-.25 1z" fill="#1c1c1c"/></svg>(02) 9555 0148
</div>
<div class="contact-item" style="top:3838px">
  <svg width="28" height="28" viewBox="0 0 24 24"><path d="M2 8l10-6 10 6v12H2z" fill="#1c1c1c"/><path d="M4 9l8 5 8-5" fill="none" stroke="var(--lime)" stroke-width="1.5"/></svg>hello@harbourgate-earth.example
</div>
<div class="contact-item" style="top:3904px">
  <svg width="28" height="28" viewBox="0 0 24 24"><path d="M12 2a7 7 0 0 0-7 7c0 5 7 13 7 13s7-8 7-13a7 7 0 0 0-7-7z" fill="#1c1c1c"/><circle cx="12" cy="9" r="2.6" fill="var(--lime)"/></svg>14 Quarry Lane, Marrickville
</div>

<div class="foot-rule"></div>
<div class="foot-small" style="left:99px">Copyright © 2025, All Rights Reserved.</div>
<div class="foot-small" style="left:822px">Privacy Policy | Term &amp; Conditions</div>

</body>
</html>
```